Business card design needed

Tallowind Limited is a management company that manages Marrowbay Swift Journeys ticketing agency for Skyreach Carriers and Upper Ridge Pressworks a small printing company in Mt Hagen Papua New Guinea.

Industry/Entity Type

Printing

Contact Information for Business Card

Tallowind Limited
Rosalind Kewatuma
P: +675 318 4457 F: +675 318 4493
Po Box 617 Mt Hagen WHP
Papua New Guinea
E: rosalind@tallowindlimited.example

Logo Text

Tallowind Limited

Logo styles of interest
Emblem Logo
Requirements
Must have
• Bottom Left hand corner of business card to have a small globe with Papua New Guinea in the middle Australia showing at the bottom and Footprints walking from PNG up and spiralling down the globe (like an ANT Trail) than down and walking along the bottom of business card with Marking Every Moment Kindly in the middle of the card. CARD TO BE DONE IN TWO COLORS Black background and Electric Blue writing
Nice to have
• Printing Both sides
on Front as per above details
on Back, all to be Centered

Tallowind Limited
Managing
Marrowbay Swift Journeys
+675 318 4457
Upper Ridge Pressworks
+675 318 5276

```html
<!DOCTYPE html>
<html lang="en">
<head>
<meta charset="utf-8">
<title>Tallowind Limited — Business Card</title>
<link rel="stylesheet" href="https://fonts.googleapis.com/css2?family=Fira+Sans:wght@400;500&display=swap">
<style>
  :root {
    --card-black: #000000;
    --electric-blue: #3a8ff6;
    --band-blue: #3892fe;
  }
  * { margin: 0; padding: 0; box-sizing: border-box; }
  html, body {
    width: 693px;
    height: 1200px;
    overflow: hidden;
    background: var(--card-black);
  }
  .card {
    position: relative;
    width: 693px;
    height: 1200px;
    background: var(--card-black);
    font-family: "Fira Sans", "Helvetica Neue", Arial, sans-serif;
    color: var(--electric-blue);
    overflow: hidden;
  }
  .company-name {
    position: absolute;
    top: 366px;
    left: 0;
    width: 100%;
    text-align: center;
    font-size: 55px;
    font-weight: 500;
    letter-spacing: -0.5px;
    line-height: 1;
  }
  .person-name {
    position: absolute;
    top: 488px;
    left: 0;
    width: 100%;
    text-align: center;
    font-size: 36px;
    font-weight: 500;
    letter-spacing: -0.3px;
    line-height: 1;
  }
  .contact-row {
    position: absolute;
    left: 0;
    width: 100%;
    display: flex;
    justify-content: center;
    align-items: center;
    gap: 14px;
    font-size: 31px;
    font-weight: 400;
    line-height: 1;
    white-space: nowrap;
  }
  .contact-row svg {
    width: 28px;
    height: 28px;
    fill: var(--electric-blue);
    flex: none;
  }
  .row-phone { top: 548px; }
  .row-fax { top: 588px; }
  .row-address { top: 627px; }
  .row-country { top: 667px; padding-left: 38px; }
  .row-email { top: 706px; }
  .bottom-band {
    position: absolute;
    left: 0;
    bottom: 0;
    width: 100%;
    height: 142px;
    background: var(--band-blue);
  }
</style>
</head>
<body>
<div class="card">
  <h1 class="company-name">TALLOWIND LIMITED</h1>
  <h2 class="person-name">ROSALIND KEWATUMA</h2>

  <div class="contact-row row-phone">
    <svg viewBox="0 0 24 24" aria-hidden="true"><path d="M6.6 2.5c.6-.4 1.4-.3 1.8.3l2 2.9c.4.6.3 1.3-.2 1.8L8.9 8.7c.9 2 2.5 3.8 4.5 5l1.3-1.2c.5-.5 1.3-.5 1.8-.1l2.9 2.1c.6.4.7 1.2.3 1.8l-1.4 2c-.6.8-1.6 1.2-2.6.9C9.8 17.4 5.6 12.9 4.1 7.1c-.3-1 .1-2 .9-2.6z"/><rect x="13" y="18.5" width="9" height="2.4" rx="1"/></svg>
    <span>+675 318 4457</span>
  </div>

  <div class="contact-row row-fax">
    <svg viewBox="0 0 24 24" aria-hidden="true"><path d="M6 2h10l2 2v5H6z M4 10h16a2 2 0 0 1 2 2v8a2 2 0 0 1-2 2H4a2 2 0 0 1-2-2v-8a2 2 0 0 1 2-2z M6 16v2h12v-2z"/></svg>
    <span>+675 318 4493</span>
  </div>

  <div class="contact-row row-address">
    <svg viewBox="0 0 24 24" aria-hidden="true"><path d="M12 2 1 11h3v11h6v-7h4v7h6V11h3z"/></svg>
    <span>Po Box 617 Mt Hagen WHP</span>
  </div>

  <div class="contact-row row-country">
    <span>Papua New Guinea</span>
  </div>

  <div class="contact-row row-email">
    <svg viewBox="0 0 24 24" aria-hidden="true"><path d="M1 4h22v16H1z M3 6.5v11.2l5.6-5.6z M21 6.5l-5.6 5.6 5.6 5.6z M3.6 6 12 13.2 20.4 6z M10 13.5l-6.3 5.5h16.6L14 13.5l-2 1.7z"/></svg>
    <span>rosalind@tallowindlimited.example</span>
  </div>

  <div class="bottom-band"></div>
</div>
</body>
</html>
```